Illustrationen für Unternehmensberatung im Bereich der Vorsorge- und Notfallplanung
ich bin hoch zufrieden mit dem Ergebnis. Vor allem ging alles ganz schnell und unkompliziert. Danke auch an dieser Stelle an Marek :-)
Zielgruppe
wir beraten kleine und mittelständige Unternehmer/Innen im Bereich der Vorsorge- und Notfallplanung, sowohl im privaten wie im betrieblichen Bereich.
Aufgabenstellung
Die Illustrationen sollten das Niveau von freiberuflich, selbständig Tätigen und von Unternehmern treffen. Nicht zu verspielt, seriös und für eine Zielgruppe ab 35 Jahren geeignet.

```html
<!DOCTYPE html>
<html lang="de">
<head>
<meta charset="utf-8">
<title>Vorsorge-Dokumente</title>
<link rel="stylesheet" href="https://fonts.googleapis.com/css2?family=Open+Sans:wght@400&display=swap">
<style>
  :root {
    --bg-deep: #0f4f6e;
    --bg-mid: #1b6f94;
    --bg-light: #2a86ad;
    --sheet: #ffffff;
    --sheet-edge: #f2f2f2;
    --ink: #262626;
  }
  html, body {
    margin: 0;
    padding: 0;
    width: 1200px;
    height: 1200px;
    overflow: hidden;
    background: var(--bg-deep);
  }
  .document-stack {
    display: block;
    width: 1200px;
    height: 1200px;
  }
  .sheet-title {
    font-family: "Open Sans", Arial, sans-serif;
    font-size: 15.5px;
    fill: var(--ink);
  }
  .sheet { fill: var(--sheet); }
</style>
</head>
<body>
<svg class="document-stack" viewBox="0 0 568 568" xmlns="http://www.w3.org/2000/svg">
  <defs>
    <radialGradient id="backdrop-tone" cx="0.55" cy="0.3" r="0.8">
      <stop offset="0" stop-color="var(--bg-light)"/>
      <stop offset="0.55" stop-color="var(--bg-mid)"/>
      <stop offset="1" stop-color="var(--bg-deep)"/>
    </radialGradient>
    <linearGradient id="paper-tone" x1="0" y1="0" x2="1" y2="1">
      <stop offset="0" stop-color="var(--sheet)"/>
      <stop offset="1" stop-color="var(--sheet-edge)"/>
    </linearGradient>
    <filter id="sheet-shadow" x="-20%" y="-20%" width="140%" height="140%">
      <feDropShadow dx="-4" dy="4" stdDeviation="4" flood-color="#000" flood-opacity="0.5"/>
    </filter>
  </defs>

  <rect class="backdrop" role="img" aria-label="Unscharfes Foto einer Beratungssituation in Blautönen" x="0" y="0" width="568" height="568" fill="url(#backdrop-tone)"/>

  <g class="sheet-group" filter="url(#sheet-shadow)">
    <polygon class="sheet" fill="url(#paper-tone)" points="30,82 388,62 433,620 73,620"/>
  </g>
  <text class="sheet-title" x="208" y="106" text-anchor="middle" transform="rotate(-3 208 101)">Patientenverfügung</text>

  <g class="sheet-group" filter="url(#sheet-shadow)">
    <polygon class="sheet" fill="url(#paper-tone)" points="78,135 437,113 478,620 117,620"/>
  </g>
  <text class="sheet-title" x="254" y="159" text-anchor="middle" transform="rotate(-3 254 154)">Betreuungsverfügung</text>

  <g class="sheet-group" filter="url(#sheet-shadow)">
    <polygon class="sheet" fill="url(#paper-tone)" points="122,190 482,170 518,620 156,620"/>
  </g>
  <text class="sheet-title" x="286" y="217" text-anchor="middle" transform="rotate(-3 286 212)">Vorsorge-Vollmacht</text>

  <g class="sheet-group" filter="url(#sheet-shadow)">
    <polygon class="sheet" fill="url(#paper-tone)" points="167,245 525,227 556,620 197,620"/>
  </g>
  <text class="sheet-title" x="340" y="272" text-anchor="middle" transform="rotate(-3 340 267)">Sorgerechts-Vollmacht</text>

  <g class="sheet-group" filter="url(#sheet-shadow)">
    <polygon class="sheet" fill="url(#paper-tone)" points="216,300 580,282 607,620 242,620"/>
  </g>
  <text class="sheet-title" x="380" y="329" text-anchor="middle" transform="rotate(-3 380 324)">Erbrecht</text>

  <g class="sheet-group" filter="url(#sheet-shadow)">
    <polygon class="sheet" fill="url(#paper-tone)" points="262,355 590,338 612,620 283,620"/>
  </g>
  <text class="sheet-title" x="438" y="384" text-anchor="middle" transform="rotate(-3 438 379)">Testament</text>
</svg>
</body>
</html>
```